wine trade consumer promotion in retail stores in the Bahamas

We need to create a poster that calls clients to action. We are a wine company in the Bahamas that needs to come across as the place to buy wines. It needs to be very authoritative and clear. that this is about making time for wine and you can try before you buy. So make Time For Wine is the lead message with graphics and the - wine of the month...try before you buy is the 2nd element.
Updates
I need ideas by Sunday 3rd October please .
Thank you
Target Market(s)
Local affluent clientele
Industry/Entity Type
wine
Other font styles liked:
- let the designer choose- look at wine companies website
Requirements
Must have
- The heading must be ¨Make Time For Wine¨ , secondary message ¨Wine Of The Month- Try Before you Buy¨- Try before you buy¨ Lots of wine images not bottles but grapes red /white,
Nice to have
- Images from vineyards around the parameters, clear messages that make you think about wine. Look at wine production sites to get an idea.
Should not have
- no palm trees or anything to do with the Caribbean, no people , no sunshine, no beaches.

```html
<!DOCTYPE html>
<html lang="en">
<head>
<meta charset="utf-8">
<title>Make Time for Wine – Wine of the Month</title>
<link rel="stylesheet" href="https://fonts.googleapis.com/css2?family=Montserrat:wght@200;300;400;700;800&display=swap">
<style>
  :root {
    --plum-deep: #3b2c6b;
    --plum-tint: #3d3274;
    --lavender: #a596d8;
    --white: #ffffff;
  }
  html, body {
    margin: 0;
    padding: 0;
    overflow: hidden;
    background: #e9e6ef;
  }
  .poster {
    position: relative;
    width: 848px;
    height: 1200px;
    overflow: hidden;
  }
  .poster svg { display: block; }
  .headline-bold { font-family: "Montserrat", sans-serif; font-weight: 800; fill: var(--white); }
  .headline-light { font-family: "Montserrat", sans-serif; font-weight: 300; }
  .accent-lavender { fill: var(--lavender); }
  .accent-plum { fill: var(--plum-deep); }
  .light-white { fill: var(--white); }
  .subline { font-family: "Montserrat", sans-serif; font-weight: 200; fill: var(--white); }
  .subline-bold { font-weight: 800; fill: var(--plum-deep); }
  .tint-panel { fill: var(--plum-tint); }
  .cta-box { fill: var(--plum-tint); opacity: 0.92; }
  .cta-text { font-family: "Montserrat", sans-serif; font-weight: 400; fill: var(--white); }
</style>
</head>
<body>
<div class="poster">
  <svg width="848" height="1200" viewBox="0 0 848 1200" xmlns="http://www.w3.org/2000/svg">
    <defs>
      <radialGradient id="grapes-top" cx="0.22" cy="0.35" r="0.85">
        <stop offset="0" stop-color="#5a5a9a"/>
        <stop offset="0.35" stop-color="#3e3c78"/>
        <stop offset="0.7" stop-color="#514a6e"/>
        <stop offset="1" stop-color="#2e2a55"/>
      </radialGradient>
      <radialGradient id="grapes-mid" cx="0.3" cy="0.55" r="0.75">
        <stop offset="0" stop-color="#6f9aa2"/>
        <stop offset="0.4" stop-color="#3f6472"/>
        <stop offset="0.75" stop-color="#31474e"/>
        <stop offset="1" stop-color="#5f6a48"/>
      </radialGradient>
      <radialGradient id="grapes-low" cx="0.35" cy="0.3" r="0.9">
        <stop offset="0" stop-color="#5e5e98"/>
        <stop offset="0.5" stop-color="#403c74"/>
        <stop offset="1" stop-color="#4b3f72"/>
      </radialGradient>
      <linearGradient id="vineyard-blur" x1="0" y1="0" x2="0.4" y2="1">
        <stop offset="0" stop-color="#8c8a5e"/>
        <stop offset="0.35" stop-color="#5d6b43"/>
        <stop offset="0.65" stop-color="#707a4c"/>
        <stop offset="1" stop-color="#8e8d60"/>
      </linearGradient>
      <linearGradient id="vineyard-bright" x1="0" y1="0" x2="0.3" y2="1">
        <stop offset="0" stop-color="#f2f4f0"/>
        <stop offset="0.14" stop-color="#c9d8bd"/>
        <stop offset="0.35" stop-color="#86a866"/>
        <stop offset="0.6" stop-color="#53683f"/>
        <stop offset="0.85" stop-color="#3a4630"/>
        <stop offset="1" stop-color="#5a5a48"/>
      </linearGradient>
      <linearGradient id="barrel" x1="0" y1="0" x2="0" y2="1">
        <stop offset="0" stop-color="#8a7a6e"/>
        <stop offset="0.5" stop-color="#8b6e5c"/>
        <stop offset="1" stop-color="#6a4a38"/>
      </linearGradient>
    </defs>

    <!-- Photo areas -->
    <rect x="0" y="0" width="646" height="496" fill="url(#grapes-top)" role="img" aria-label="Close-up of dark red grape bunches and vine leaves"/>
    <rect x="0" y="496" width="646" height="195" fill="url(#grapes-mid)" role="img" aria-label="Blue-black grapes hanging on the vine"/>
    <rect x="0" y="691" width="325" height="509" fill="url(#grapes-low)" role="img" aria-label="Grape bunch on the vine"/>
    <rect x="325" y="691" width="321" height="509" fill="url(#vineyard-blur)" role="img" aria-label="Soft-focus vineyard rows"/>
    <rect x="646" y="0" width="202" height="884" fill="url(#vineyard-bright)" role="img" aria-label="Sunlit vineyard with a wine bottle among the vines"/>
    <rect x="646" y="884" width="202" height="316" fill="url(#barrel)" role="img" aria-label="Oak wine barrel staves"/>

    <!-- Plum tint panels -->
    <rect class="tint-panel" x="0" y="0" width="646" height="496" opacity="0.45"/>
    <rect class="tint-panel" x="0" y="691" width="325" height="509" opacity="0.5"/>

    <!-- Lead message -->
    <text class="headline-bold" x="131" y="453" font-size="100">Make tim</text>
    <text class="headline-light accent-lavender" x="624" y="506" font-size="178">e</text>
    <text class="headline-bold" x="131" y="563" font-size="100">for</text>
    <text class="headline-light" x="329" y="638" font-size="213"><tspan class="light-white">wi</tspan><tspan class="accent-plum">ne</tspan></text>

    <!-- Secondary message -->
    <text class="subline" x="157" y="737" font-size="70">Wine of the mo<tspan class="subline-bold">nth</tspan></text>

    <!-- Call to action -->
    <rect class="cta-box" x="522" y="812" width="326" height="74"/>
    <text class="cta-text" x="533" y="858" font-size="32.5">Try before you buy</text>
  </svg>
</div>
</body>
</html>
```